Brochure Cover Design Project

Need a design for our company brochure cover.
We are a mechanical consulting engineering firm ( HVAC, pLUMBING). We have the brochure

Target Market(s)

Architects and Building Owners

Industry/Entity Type

Hvac

```html
<!DOCTYPE html>
<html lang="en">
<head>
<meta charset="utf-8">
<title>Brochure Cover – Northfield Building Systems</title>
<link href="https://fonts.googleapis.com/css2?family=Quicksand:wght@500;700&display=swap" rel="stylesheet">
<style>
  :root {
    --green-deep: #1b5e20;
    --green-mid: #3f7f35;
    --green-light: #7cb342;
    --green-bar: #2f6b25;
    --silver-light: #f8f8f8;
    --silver-edge: #d4d5d6;
    --white: #ffffff;
    --spine: #a9aaab;
    --page-bg: #d9d9d9;
  }
  * { box-sizing: border-box; margin: 0; padding: 0; }
  html, body { width: 1200px; height: 947px; overflow: hidden; background: var(--page-bg); }
  .spread {
    position: relative; width: 1200px; height: 947px; display: flex;
    font-family: "Quicksand", sans-serif; color: var(--white);
  }
  .panel { position: relative; width: 600px; height: 947px; overflow: hidden; }
  .panel + .panel { border-left: 1px solid var(--spine); }
  .texture {
    position: absolute; inset: 0;
    background:
      radial-gradient(ellipse at 50% 30%, var(--white) 0%, rgba(255,255,255,0) 55%),
      radial-gradient(ellipse at 50% 80%, var(--white) 0%, rgba(255,255,255,0) 50%),
      linear-gradient(90deg, var(--silver-edge) 0%, var(--silver-light) 40%, var(--silver-light) 60%, var(--silver-edge) 100%);
  }
  .bar-top {
    position: absolute; left: 0; right: 0; top: 50px; height: 17px;
    background: linear-gradient(90deg, var(--green-bar) 0%, var(--green-light) 50%, var(--green-bar) 100%);
  }
  .rule { position: absolute; left: 0; right: 0; height: 4px; background: var(--green-mid); }
  .rule-upper { top: 314px; }
  .rule-lower { top: 627px; }
  .band-main {
    position: absolute; left: 0; right: 0; top: 329px; height: 289px;
    background: radial-gradient(ellipse at 50% 45%, var(--green-mid) 0%, #357a30 35%, var(--green-deep) 100%);
    border-top: 2px solid var(--green-bar);
  }
  .band-foot {
    position: absolute; left: 0; right: 0; top: 844px; height: 54px;
    background: radial-gradient(ellipse at 50% 50%, var(--green-mid) 0%, var(--green-deep) 100%);
    border-top: 2px solid var(--green-light); border-bottom: 3px solid var(--green-light);
    display: flex; align-items: center; justify-content: center;
    font-size: 18px; font-weight: 500; letter-spacing: 0.3px;
  }
  .contact { position: absolute; left: 0; right: 0; top: 402px; text-align: center; }
  .contact-name { font-size: 15.5px; font-weight: 700; letter-spacing: 0.2px; margin-bottom: 18px; }
  .contact-line { font-size: 14px; font-weight: 500; line-height: 21px; }
  .contact-gap { height: 18px; }
  .logo-plate {
    position: absolute; left: 99px; top: 414px; width: 387px; height: 118px;
    background: linear-gradient(180deg, var(--white) 0 63%, #4e8c40 63% 100%);
    box-shadow: 0 3px 10px rgba(0,0,0,0.35);
    display: flex; align-items: center; justify-content: center;
  }
  .logo-name {
    font-family: "Quicksand", sans-serif; font-weight: 700; font-size: 40px;
    color: var(--green-deep); letter-spacing: 1px; margin-top: -22px;
  }
</style>
</head>
<body>
<main class="spread">
  <section class="panel panel-back">
    <div class="texture" role="img" aria-label="Soft silver background with faint technical grid pattern"></div>
    <div class="bar-top"></div>
    <div class="rule rule-upper"></div>
    <div class="band-main"></div>
    <div class="contact">
      <p class="contact-name">NORTHFIELD BUILDING SYSTEMS inc.</p>
      <p class="contact-line">2450 Harbor Way Ste. 210</p>
      <p class="contact-line">Cedar Point, CA 90210</p>
      <div class="contact-gap"></div>
      <p class="contact-line">P:&nbsp; 555-014-0172 x 214</p>
      <p class="contact-line">F:&nbsp; 555-014-0189</p>
    </div>
    <div class="rule rule-lower"></div>
    <div class="band-foot">www.northfield-bs.com</div>
  </section>
  <section class="panel panel-front">
    <div class="texture" role="img" aria-label="Soft silver background with faint technical grid pattern"></div>
    <div class="bar-top"></div>
    <div class="rule rule-upper"></div>
    <div class="band-main"></div>
    <div class="logo-plate"><span class="logo-name">NORTHFIELD</span></div>
    <div class="rule rule-lower"></div>
    <div class="band-foot">Designing Systems That Perform.</div>
  </section>
</main>
</body>
</html>
```